Graphics for Technology Company's Pennaroo Page

Need someone to create some graphics for our Pennaroo company page.
In particular, we're looking for:
- cover image
- Image for "overview"
- Image for "life"

I'd like you to take our logo and create professional graphics for our company Pennaroo page (https://www.pennaroo.net/company/7395081/).

Some examples of pages recognized by Pennaroo as top quality:
https://www.pennaroo.net/company/8574/
https://www.pennaroo.net/company/4718/
https://www.pennaroo.net/company/53720946/
https://www.pennaroo.net/company/8047352/

I especially like the last- zelquin. This is the kind of feel I'm looking for.

Target Market(s)

Medium and large businesses

Industry/Entity Type

Information Technology

Requirements
Must have
• The header should be proportional to 1536x768. Must use at least some of the colors in the logo and elements of the logo.
• Please note, this should be three distinct and thematically related images.

```html
<!DOCTYPE html>
<html lang="en">
<head>
<meta charset="UTF-8">
<title>Cover – We turn your data into Dollars</title>
<link rel="stylesheet" href="https://fonts.googleapis.com/css2?family=Ropa+Sans&display=swap">
<style>
  :root {
    --page-bg: #ffffff;
    --brand-green: #86b83c;
    --brand-green-light: #9cc95a;
    --brand-green-deep: #6f9e2c;
    --ink-light: #ffffff;
    --bar-tint: rgba(255, 255, 255, 0.45);
    --pattern-tint: rgba(255, 255, 255, 0.18);
  }

  html, body {
    margin: 0;
    padding: 0;
    width: 1200px;
    height: 900px;
    overflow: hidden;
    background: var(--page-bg);
  }

  .canvas {
    position: relative;
    width: 1200px;
    height: 900px;
    background: var(--page-bg);
  }

  .cover-banner {
    position: absolute;
    left: 49px;
    top: 175px;
    width: 1102px;
    height: 551px;
    overflow: hidden;
  }

  .cover-photo {
    position: absolute;
    inset: 0;
    background:
      radial-gradient(ellipse at 70% 15%, var(--brand-green-deep) 0%, transparent 45%),
      radial-gradient(ellipse at 20% 10%, var(--brand-green-deep) 0%, transparent 35%),
      linear-gradient(180deg, var(--brand-green) 0%, var(--brand-green-light) 100%);
  }

  .dot-pattern {
    position: absolute;
    left: 0;
    top: 202px;
    width: 365px;
    height: 279px;
    background: var(--pattern-tint);
    border-radius: 0 24px 24px 0;
  }

  .speed-bar {
    position: absolute;
    left: 411px;
    width: 300px;
    height: 42px;
    border-radius: 21px;
    background: linear-gradient(90deg, var(--bar-tint) 0%, rgba(255,255,255,0.28) 55%, rgba(255,255,255,0) 100%);
  }
  .speed-bar--top { top: 200px; }
  .speed-bar--middle { top: 319px; width: 280px; }
  .speed-bar--bottom { top: 434px; }

  .tagline {
    position: absolute;
    left: 396px;
    top: 243px;
    margin: 0;
    font-family: "Ropa Sans", "Helvetica Neue", Arial, sans-serif;
    font-weight: 400;
    font-size: 78px;
    line-height: 75px;
    color: var(--ink-light);
    text-shadow: 2px 3px 5px rgba(40, 60, 10, 0.45);
    letter-spacing: -0.5px;
  }
  .tagline__line {
    display: block;
    white-space: nowrap;
  }
  .tagline__line--second {
    padding-left: 304px;
  }
</style>
</head>
<body>
  <main class="canvas">
    <section class="cover-banner" aria-label="Company page cover">
      <div class="cover-photo" role="img" aria-label="Green-tinted photo of a business meeting with a laptop, glasses, a smartphone and printed charts on a desk"></div>
      <div class="dot-pattern" role="img" aria-label="Dot-grid pattern"></div>
      <div class="speed-bar speed-bar--top"></div>
      <div class="speed-bar speed-bar--middle"></div>
      <div class="speed-bar speed-bar--bottom"></div>
      <h1 class="tagline">
        <span class="tagline__line">We turn your data</span>
        <span class="tagline__line tagline__line--second">into Dollars</span>
      </h1>
    </section>
  </main>
</body>
</html>
```